TAVRO Capital Group LLC a High Risk Big Rewards company for Rich Young Entrepreneurs

We would like a very modern, powerful in the eyes of our customers, modern, minimalist feel, financial gain. this business card is for young Rich entrepreneurs who want to invest money into High Risk, Big Rewards Businesses. The card Should sell the business!! let your creativity go Wild! I pick most of the designers for this project because of your BOLD Designs, I would like this card to be Bold, Modern, Minimalist, use as many effects in your graphic Artist Mind, Do not let the Financial sound of this business to make you think Conservative that's the last thing we are! if you have a lot of money and you want to play a risky market call US
Updates

Project Deadline Extended
Reason: have not received, enough designs to choose 1st and second place, sure I have received over 100 designs but it seems most designers are submitting every card they have ever made before and calling it mine, please we are looking for fresh ideas please!

Target Market(s)

Private Risky Investors

Industry/Entity Type

Financial

Contact Information for Business Card

powerful in the eyes of our customers,modern, minimalist feel

Font styles to use
Other font styles liked:
• Modern feeling fonts

Requirements
Must have
• The Company Name is TAVRO Capital Group LLC and it must be on the CARD
• My Name, title, Cell , email
• Delvin Ashcroft G.E.D.
• Managing Member
• 555.038.6195
• delvin@tavrocapitalgroup.example
Nice to have
• try a black thick plastic card with round corners with Delvin Ashcroft GED (make sure GED is smaller than name) just on one side of the card, and my phone number with out the icons and email on the other side, this card should look like a exclusive credit card or exclusive VIP card, something you would never loose

```html
<!DOCTYPE html>
<html lang="en">
<head>
<meta charset="utf-8">
<title>TAVRO Capital Group LLC – Business Card</title>
<link rel="stylesheet" href="https://fonts.googleapis.com/css2?family=Montserrat:wght@700;800&family=Rubik:wght@500&family=Source+Sans+3:ital,wght@0,400;0,600;1,400&display=swap">
<style>
  :root {
    --ink: #1f1f1f;
    --paper: #ffffff;
    --brand-blue: #009fe3;
    --texture-grey: #8a8a8a;
    --texture-dark: #6b6a68;
    --card-shadow: 0 14px 22px rgba(0,0,0,0.22);
  }
  * { margin: 0; padding: 0; box-sizing: border-box; }
  html, body { width: 927px; height: 1200px; overflow: hidden; background: var(--paper); }
  .canvas { position: relative; width: 927px; height: 1200px; background: var(--paper); }

  /* Front card */
  .card-front {
    position: absolute; left: 138px; top: 222px; width: 654px; height: 338px;
    box-shadow: var(--card-shadow); background: var(--paper);
  }
  .brand-mark {
    position: absolute; left: 0; top: 0; width: 312px; height: 64px;
    background: var(--paper); display: flex; align-items: flex-end; justify-content: center;
    font-family: "Montserrat", sans-serif; font-weight: 800; font-size: 66px;
    line-height: 0.8; color: var(--ink); letter-spacing: -1px; overflow: hidden;
  }
  .texture-left {
    position: absolute; left: 0; top: 63px; width: 312px; height: 275px;
    background: linear-gradient(135deg, var(--texture-grey), var(--texture-dark) 50%, var(--texture-grey));
  }
  .info-panel {
    position: absolute; left: 312px; top: 0; width: 342px; height: 338px; background: var(--ink);
  }
  .texture-right {
    position: absolute; left: 163px; top: 63px; width: 179px; height: 114px;
    background: linear-gradient(135deg, var(--texture-grey), var(--texture-dark) 50%, var(--texture-grey));
  }
  .company-name {
    position: absolute; left: 16px; top: 14px;
    font-family: "Montserrat", sans-serif; font-weight: 700; font-size: 27px;
    color: var(--paper); letter-spacing: -0.5px; white-space: nowrap;
  }
  .company-name small { font-size: 17px; font-weight: 700; letter-spacing: 0; }
  .role-badge {
    position: absolute; left: 65px; top: 102px; width: 196px; height: 196px; border-radius: 50%;
    background: var(--brand-blue); display: flex; flex-direction: column; align-items: center; justify-content: center;
    font-family: "Montserrat", sans-serif; font-weight: 800; font-size: 31px; line-height: 1.1;
    color: var(--ink); text-align: center; letter-spacing: -0.5px;
  }
  .role-badge svg { width: 48px; height: 48px; margin-bottom: 8px; }
  .contact { position: absolute; left: 0; top: 0; width: 342px; height: 338px; }
  .contact-name {
    position: absolute; left: 53px; top: 195px;
    font-family: "Rubik", sans-serif; font-weight: 500; font-size: 22px;
    color: var(--brand-blue); white-space: nowrap;
  }
  .contact-name small { font-family: "Source Sans 3", sans-serif; font-weight: 400; font-size: 16px; margin-left: 4px; }
  .contact-line {
    position: absolute; left: 14px; display: flex; align-items: center; gap: 10px;
    font-family: "Source Sans 3", sans-serif; font-size: 18px; color: var(--paper); white-space: nowrap;
  }
  .contact-line svg { width: 26px; height: 26px; flex: none; }
  .line-phone { top: 224px; }
  .line-email { top: 261px; }
  .line-web { top: 290px; }

  /* Back card */
  .card-back {
    position: absolute; left: 136px; top: 690px; width: 653px; height: 332px;
    background: var(--brand-blue); box-shadow: var(--card-shadow);
  }
  .promise-list { position: absolute; left: 315px; top: 74px; list-style: none; }
  .promise-list li {
    display: flex; align-items: center; gap: 18px; height: 47px;
    font-family: "Source Sans 3", sans-serif; font-size: 29px; color: var(--paper);
  }
  .promise-list li svg { width: 40px; height: 40px; flex: none; }
  .promise-list strong { font-weight: 600; }
  .promise-list em { font-style: italic; }
</style>
</head>
<body>
<div class="canvas">

  <section class="card-front">
    <div class="brand-mark">TAVRO</div>
    <div class="texture-left" role="img" aria-label="Grey abstract tangled-line texture"></div>
    <div class="role-badge">
      <svg viewBox="0 0 48 48" aria-hidden="true"><circle cx="24" cy="24" r="21" fill="none" stroke="#fff" stroke-width="4"/><path d="M14 25l7 7 13-14" fill="none" stroke="#fff" stroke-width="5" stroke-linecap="round" stroke-linejoin="round"/></svg>
      <span>MANAGING<br>MEMBER</span>
    </div>

    <div class="info-panel">
      <div class="company-name">Capital Group <small>LLC</small></div>
      <div class="texture-right" role="img" aria-label="Grey abstract tangled-line texture"></div>
      <div class="contact">
        <div class="contact-name">Delvin Ashcroft <small>G.E.D.</small></div>
        <div class="contact-line line-phone">
          <svg viewBox="0 0 26 26" aria-hidden="true"><rect x="7" y="3" width="12" height="21" rx="3" fill="#009fe3"/><rect x="9.5" y="7" width="7" height="6" fill="#1f1f1f"/><circle cx="13" cy="19" r="1.6" fill="#1f1f1f"/><rect x="8" y="0" width="2" height="5" fill="#009fe3"/></svg>
          <span>555.038.6195</span>
        </div>
        <div class="contact-line line-email">
          <svg viewBox="0 0 26 26" aria-hidden="true"><rect x="1.5" y="5" width="23" height="16" fill="none" stroke="#009fe3" stroke-width="2"/><path d="M1.5 5l11.5 10L24.5 5M1.5 21l8-8M24.5 21l-8-8" fill="none" stroke="#009fe3" stroke-width="2"/></svg>
          <span>delvin@tavrocapitalgroup.example</span>
        </div>
        <div class="contact-line line-web">
          <svg viewBox="0 0 26 26" aria-hidden="true"><circle cx="12" cy="12" r="10.5" fill="none" stroke="#009fe3" stroke-width="2"/><ellipse cx="12" cy="12" rx="4.5" ry="10.5" fill="none" stroke="#009fe3" stroke-width="2"/><path d="M1.5 12h21M3.5 6.5h17M3.5 17.5h17" stroke="#009fe3" stroke-width="2"/><path d="M15 14l9 4-4 1.2 2.5 4-1.6 1-2.5-4-3 2.6z" fill="#009fe3" stroke="#1f1f1f" stroke-width="0.8"/></svg>
          <span>www.tavrocapitalgroup.example</span>
        </div>
      </div>
    </div>
  </section>

  <section class="card-back">
    <ul class="promise-list">
      <li><svg viewBox="0 0 40 40" aria-hidden="true"><circle cx="20" cy="20" r="17.5" fill="none" stroke="#fff" stroke-width="3.5"/><path d="M11.5 21l6 6 11-12" fill="none" stroke="#fff" stroke-width="4.5" stroke-linecap="round" stroke-linejoin="round"/></svg><em>big risks big gains</em></li>
      <li><svg viewBox="0 0 40 40" aria-hidden="true"><circle cx="20" cy="20" r="17.5" fill="none" stroke="#fff" stroke-width="3.5"/><path d="M11.5 21l6 6 11-12" fill="none" stroke="#fff" stroke-width="4.5" stroke-linecap="round" stroke-linejoin="round"/></svg><span><strong>GAIN</strong> finance</span></li>
      <li><svg viewBox="0 0 40 40" aria-hidden="true"><circle cx="20" cy="20" r="17.5" fill="none" stroke="#fff" stroke-width="3.5"/><path d="M11.5 21l6 6 11-12" fill="none" stroke="#fff" stroke-width="4.5" stroke-linecap="round" stroke-linejoin="round"/></svg><span><strong>BIG</strong> rewards</span></li>
      <li><svg viewBox="0 0 40 40" aria-hidden="true"><circle cx="20" cy="20" r="17.5" fill="none" stroke="#fff" stroke-width="3.5"/><path d="M11.5 21l6 6 11-12" fill="none" stroke="#fff" stroke-width="4.5" stroke-linecap="round" stroke-linejoin="round"/></svg><span><strong>HIGH</strong> returns</span></li>
      <li><svg viewBox="0 0 40 40" aria-hidden="true"><circle cx="20" cy="20" r="17.5" fill="none" stroke="#fff" stroke-width="3.5"/><path d="M11.5 21l6 6 11-12" fill="none" stroke="#fff" stroke-width="4.5" stroke-linecap="round" stroke-linejoin="round"/></svg><span><strong>INVEST</strong> in us</span></li>
    </ul>
  </section>

</div>
</body>
</html>
```